Business cards and stationary design

We just completed the design of our new logo and we need to print new business cards and letterhead for our nonprofit. We are looking for a fresh new design that shows off our new logo. On letterhead, we must have a column on the right or left to include our Board of Directors (up to 45 names) (see attachment)

Industry/Entity Type

Non-Profit

Contact Information for Business Card

Standard business card with name, title, Company name, mailing address phone numbers, email address and website. Tagline on back "Bringing the homeless home"

Font styles to use
Sans Serif

Requirements
Must have
• include pertinent information above
• new logo
• fonts compatible with logo
• should use logo colors only
Nice to have
• tag lines

```html
<!DOCTYPE html>
<html lang="en">
<head>
<meta charset="utf-8">
<title>Homeward Relief Center – Business Card</title>
<link href="https://fonts.googleapis.com/css2?family=Michroma&family=Oswald:wght@400&display=swap" rel="stylesheet">
<style>
  :root {
    --brand-red: #ed1c24;
    --brand-teal: #037e9e;
    --brand-yellow: #fbb62b;
    --paper: #ffffff;
    --card-edge: #d4d4d4;
    --faint-teal: #e3f0f4;
  }
  * { margin: 0; padding: 0; box-sizing: border-box; }
  html, body { width: 1200px; height: 1200px; overflow: hidden; background: var(--paper); }
  .canvas { position: relative; width: 1200px; height: 1200px; }

  .card {
    position: absolute; left: 171px; width: 877px; height: 500px;
    background: var(--paper); border: 2px solid var(--card-edge); overflow: hidden;
  }
  .card--front { top: 49px; }
  .card--back { top: 626px; }

  /* Front */
  .brand { position: absolute; left: 0; top: 0; width: 605px; height: 393px; text-align: center; }
  .brand__dot {
    position: absolute; left: 272px; top: 90px; width: 62px; height: 62px;
    border-radius: 50%; background: var(--brand-yellow);
  }
  .brand__name {
    position: absolute; left: 0; right: 0; top: 178px;
    font-family: "Michroma", sans-serif; font-size: 33px; line-height: 1.3;
    letter-spacing: 4px; color: var(--brand-teal);
  }
  .brand__rule {
    position: absolute; left: 42px; right: 42px; top: 318px; height: 2px; background: var(--brand-red);
  }

  .contact-panel {
    position: absolute; right: 0; top: 0; width: 274px; height: 393px;
    background: var(--brand-red); color: var(--paper);
    font-family: "Oswald", sans-serif; padding: 60px 0 0 34px;
  }
  .contact-panel__name { font-size: 27px; line-height: 1.2; }
  .contact-panel__title { font-size: 20px; line-height: 1.4; margin-bottom: 30px; }
  .contact-panel__line { font-size: 21px; line-height: 34px; }
  .contact-panel__key { color: var(--brand-yellow); margin-right: 4px; }
  .contact-panel__address { margin-top: 21px; }

  .web-band {
    position: absolute; left: 0; right: 0; bottom: 0; height: 107px;
    background: var(--brand-teal); text-align: center;
    font-family: "Michroma", sans-serif; font-size: 16px; letter-spacing: 4px; padding-top: 25px;
  }
  .web-band__email { color: var(--paper); line-height: 30px; }
  .web-band__site { color: var(--brand-yellow); line-height: 28px; }

  /* Back */
  .back-accent {
    position: absolute; left: 330px; top: 30px; width: 640px; height: 640px;
    border-radius: 50%; background: var(--faint-teal);
  }
  .tagline {
    position: absolute; left: 156px; top: 207px; white-space: nowrap;
    display: flex; align-items: baseline; gap: 26px;
  }
  .tagline__lead { font-family: "Oswald", sans-serif; font-size: 46px; color: var(--brand-red); }
  .tagline__home { font-family: "Michroma", sans-serif; font-size: 30px; letter-spacing: 3px; color: var(--brand-teal); }
</style>
</head>
<body>
<main class="canvas">
  <section class="card card--front">
    <div class="brand">
      <span class="brand__dot"></span>
      <p class="brand__name">HOMEWARD RELIEF<br>CENTER</p>
      <span class="brand__rule"></span>
    </div>

    <div class="contact-panel">
      <p class="contact-panel__name">JOHN DOE</p>
      <p class="contact-panel__title">Title</p>
      <p class="contact-panel__line"><span class="contact-panel__key">P</span>555.201.4837</p>
      <p class="contact-panel__line"><span class="contact-panel__key">C</span>555.318.6290</p>
      <p class="contact-panel__line"><span class="contact-panel__key">F</span>555.472.1056</p>
      <div class="contact-panel__address">
        <p class="contact-panel__line">P.O Box 482190</p>
        <p class="contact-panel__line">Dallas, TX 75208</p>
      </div>
    </div>

    <div class="web-band">
      <p class="web-band__email">JOHN@HOMEWARDRELIEFCENTER.COM</p>
      <p class="web-band__site">WWW.HOMEWARDRELIEFCENTER.COM</p>
    </div>
  </section>

  <section class="card card--back">
    <span class="back-accent"></span>
    <p class="tagline">
      <span class="tagline__lead">Bringing the homeless</span>
      <span class="tagline__home">HOME</span>
    </p>
  </section>
</main>
</body>
</html>
```